Leave-behind marketing postcard showing retirement plan limits for the last three years.

We need a 5x7 postcard for our company, Meridel Halvorsen, Inc. We are a third party retirement plan administration firm. The piece should include our logo, address, phone, website, and the contribution limits for the last three years - 2015, 2014, 2013 (see attached for company logo, color palette and retirement plan limits chart). You can also incorporate our slogan on one of the sides - "Providing and protecting retirement since 1983." This postcard is a leave-behind. We will not be mailing it so you don't have to include space for a stamp and address. The postcard can be 4 color on both sides. Include a bleed.

Target Market(s)

Financial advisors and business owners

Industry/Entity Type

Marketing

Font styles to use
Other font styles liked:
• Georgia and arial

Requirements
Must have
• Please use some of the colors in the attached color palette.

```html
<!DOCTYPE html>
<html lang="en">
<head>
<meta charset="utf-8">
<title>Meridel Halvorsen, Inc. — Retirement Plan Limits Postcard</title>
<link rel="stylesheet" href="https://fonts.googleapis.com/css2?family=Arimo:wght@400;700&display=swap">
<style>
  :root {
    --backdrop: #848484;
    --navy: #13123f;
    --brand-blue: #1b5a86;
    --teal: #6aacb0;
    --cell-grey: #d2d5d8;
    --taupe: #a99b93;
    --photo-top: #3d6c9e;
    --photo-bottom: #9aa28a;
    --banner-left: #1d3f6e;
    --banner-right: #6f8fb8;
    --white: #ffffff;
    --ink: #111111;
  }
  * { box-sizing: border-box; margin: 0; padding: 0; }
  html, body { width: 927px; height: 1200px; overflow: hidden; }
  body { background: var(--backdrop); font-family: "Arimo", Arial, sans-serif; position: relative; }

  .card { position: absolute; left: 76px; width: 775px; height: 561px; overflow: hidden; background: var(--white); }
  .card--front { top: 29px; }
  .card--back { top: 605px; }

  /* Front */
  .front-art { position: absolute; inset: 0; }
  .slogan {
    position: absolute; left: 97px; top: 67px; width: 580px; height: 51px;
    background: rgba(27, 90, 134, 0.92); color: var(--white);
    font-weight: 700; font-size: 19.5px; letter-spacing: 0.2px;
    display: flex; align-items: center; justify-content: center;
  }
  .brand-front {
    position: absolute; left: 49px; top: 448px; width: 190px;
    color: var(--white); font-weight: 700; font-size: 25px; line-height: 1.15;
  }
  .contact-list { position: absolute; left: 243px; top: 422px; list-style: none; color: var(--white); font-size: 17.5px; }
  .contact-list li { display: flex; align-items: center; height: 21.5px; white-space: nowrap; }
  .contact-list svg { width: 14px; height: 14px; margin-right: 10px; flex: none; }

  /* Back */
  .back-header { position: absolute; left: 0; top: 0; width: 775px; height: 103px; }
  .brand-back {
    position: absolute; left: 30px; top: 28px; width: 200px;
    color: var(--white); font-weight: 700; font-size: 23px; line-height: 1.1;
  }
  .back-tagline {
    position: absolute; right: 26px; top: 23px; color: rgba(255,255,255,0.85);
    font-size: 11.5px; letter-spacing: 3px; font-weight: 700;
  }
  .limits-title {
    position: absolute; left: 0; width: 100%; top: 113px; text-align: center;
    color: var(--brand-blue); font-weight: 700; font-size: 19px;
  }
  .limits-table {
    position: absolute; left: 37px; top: 152px; width: 701px;
    border-collapse: collapse; table-layout: fixed;
  }
  .limits-table th, .limits-table td { border: 1px solid #3a3a3a; }
  .limits-table thead th {
    background: var(--taupe); color: var(--white); font-size: 9.5px; font-weight: 700;
    height: 22px; text-align: center;
  }
  .limits-table thead th.type-col { text-align: left; padding-left: 6px; width: 127px; }
  .limits-table tbody th {
    background: linear-gradient(90deg, #1b4f78, #1f6290);
    color: var(--white); font-size: 10.5px; font-weight: 700; text-align: left;
    padding: 0 6px; line-height: 1.15; height: 39px;
  }
  .limits-table sup { font-size: 7px; }
  .limits-table td { text-align: center; font-size: 10.5px; font-weight: 700; color: var(--ink); }
  .limits-table td:nth-child(even) { background: var(--cell-grey); }
  .limits-table td:nth-child(odd) { background: var(--teal); }
  .footnotes { position: absolute; left: 34px; top: 497px; font-size: 11px; line-height: 1.2; color: var(--ink); }
  .footnotes sup { font-size: 7px; }
</style>
</head>
<body>

<section class="card card--front">
  <svg class="front-art" viewBox="0 0 775 561" width="775" height="561">
    <defs>
      <linearGradient id="frontPhotoTone" x1="0" y1="0" x2="0" y2="1">
        <stop offset="0" stop-color="#3d6c9e"/>
        <stop offset="1" stop-color="#9aa28a"/>
      </linearGradient>
    </defs>
    <rect role="img" aria-label="Photo area: open road through flower fields under the sky" width="775" height="430" fill="url(#frontPhotoTone)"/>
    <polygon points="0,255 560,385 775,395 775,430 0,430" fill="#6fb0c4" opacity="0.55"/>
    <polygon points="0,300 500,370 775,410 0,430" fill="#2d6f9a" opacity="0.7"/>
    <polygon points="0,340 775,412 775,561 0,561" fill="#13123f"/>
    <polygon points="525,393 775,335 775,413" fill="#b7aca6"/>
  </svg>
  <div class="slogan">PROVIDING AND PROTECTING RETIREMENT SINCE 1983.</div>
  <div class="brand-front">Meridel Halvorsen, Inc.</div>
  <ul class="contact-list">
    <li><svg viewBox="0 0 14 14"><path d="M7 1a4 4 0 0 0-4 4c0 3 4 8 4 8s4-5 4-8a4 4 0 0 0-4-4z" fill="none" stroke="#fff" stroke-width="1.6"/><circle cx="7" cy="5" r="1.3" fill="#fff"/></svg>1840 Larkspur Ave., Suite 210, Fairhaven, California 90388</li>
    <li><svg viewBox="0 0 14 14"><path d="M1 5c2-3 10-3 12 0l-2 1.5-2-1V4.5H5v1l-2 1z" fill="#fff"/><rect x="3" y="7" width="8" height="5" rx="1" fill="#fff"/></svg>(555) 014-2600</li>
    <li><svg viewBox="0 0 14 14"><rect x="3.5" y="1" width="7" height="4" fill="#fff"/><rect x="1" y="5.5" width="12" height="5" rx="1" fill="#fff"/><rect x="3.5" y="9" width="7" height="4" fill="#fff" stroke="#13123f" stroke-width="0.8"/></svg>(555) 014-2650</li>
    <li><svg viewBox="0 0 14 14"><rect x="1" y="3" width="12" height="9" fill="#fff"/><path d="M1 3l6 5 6-5" fill="none" stroke="#13123f" stroke-width="1.2"/></svg>information@meridelbenefits.com</li>
    <li><svg viewBox="0 0 14 14"><circle cx="7" cy="7" r="6" fill="#fff"/><path d="M1 7h12M7 1c-3 3-3 9 0 12M7 1c3 3 3 9 0 12" fill="none" stroke="#13123f" stroke-width="0.9"/></svg>www.meridelbenefits.com/</li>
  </ul>
</section>

<section class="card card--back">
  <svg class="back-header" viewBox="0 0 775 103" width="775" height="103">
    <defs>
      <linearGradient id="bannerPhotoTone" x1="0" y1="0" x2="1" y2="0">
        <stop offset="0" stop-color="#1d3f6e"/>
        <stop offset="1" stop-color="#6f8fb8"/>
      </linearGradient>
    </defs>
    <rect role="img" aria-label="Photo area: pier over calm water at dusk" width="775" height="103" fill="url(#bannerPhotoTone)"/>
  </svg>
  <div class="brand-back">Meridel Halvorsen, Inc.</div>
  <div class="back-tagline">MERIDEL HALVORSEN, INC.</div>

  <h1 class="limits-title">MAXIMUM BENEFIT AND CONTRIBUTION LIMITS</h1>

  <table class="limits-table">
    <thead>
      <tr><th class="type-col">Type of Limitation</th><th>2015</th><th>2014</th><th>2013</th><th>2012</th><th>2011</th><th>2010</th><th>2009</th><th>2008</th><th>2007</th><th>2006</th><th>2005</th></tr>
    </thead>
    <tbody>
      <tr><th>401(k) / 403(b) Elective Deferrals</th><td>$18,000</td><td>$17,500</td><td>$17,500</td><td>$17,000</td><td>$16,500</td><td>$16,500</td><td>$16,500</td><td>$15,500</td><td>$15,500</td><td>$15,000</td><td>$14,000</td></tr>
      <tr><th>Catch-up amount <sup>*</sup></th><td>$6,000</td><td>$5,500</td><td>$5,500</td><td>$5,500</td><td>$5,500</td><td>$5,500</td><td>$5,500</td><td>$5,000</td><td>$5,000</td><td>$5,000</td><td>$4,000</td></tr>
      <tr><th>Defined Benefit Plans<sup>1</sup></th><td>$210,000</td><td>$210,000</td><td>$205,000</td><td>$200,000</td><td>$195,000</td><td>$195,000</td><td>$195,000</td><td>$185,000</td><td>$180,000</td><td>$175,000</td><td>$170,000</td></tr>
      <tr><th>Defined Contribution Plans<sup>1</sup></th><td>$53,000</td><td>$52,000</td><td>$51,000</td><td>$50,000</td><td>$49,000</td><td>$49,000</td><td>$49,000</td><td>$46,000</td><td>$45,000</td><td>$44,000</td><td>$42,000</td></tr>
      <tr><th>Annual Compensation Limit<sup>2</sup></th><td>$265,000</td><td>$260,000</td><td>$255,000</td><td>$250,000</td><td>$245,000</td><td>$245,000</td><td>$245,000</td><td>$230,000</td><td>$225,000</td><td>$220,000</td><td>$210,000</td></tr>
      <tr><th>Highly Compensated Employees</th><td>$120,000</td><td>$115,000</td><td>$115,000</td><td>$115,000</td><td>$110,000</td><td>$110,000</td><td>$110,000</td><td>$105,000</td><td>$100,000</td><td>$100,000</td><td>$95,000</td></tr>
      <tr><th>Key employee officer threshold<sup>1</sup></th><td>$170,000</td><td>$170,000</td><td>$165,000</td><td>$165,000</td><td>$160,000</td><td>$160,000</td><td>$160,000</td><td>$150,000</td><td>$145,000</td><td>$140,000</td><td>$135,000</td></tr>
      <tr><th>Income Subject to Social Security Tax<sup>2</sup></th><td>$118,500</td><td>$117,000</td><td>$113,700</td><td>$110,100</td><td>$106,800</td><td>$106,800</td><td>$106,800</td><td>$102,000</td><td>$97,500</td><td>$94,200</td><td>$90,000</td></tr>
    </tbody>
  </table>

  <div class="footnotes">
    <p>*For individuals age 50 and older</p>
    <p><sup>1</sup> Based on plan year ending in calendar year</p>
    <p><sup>2</sup> Based on plan year beginning in calendar year</p>
  </div>
</section>

</body>
</html>
```